依頼概要
■依頼の目的/概要
友人の結婚式招待状の作成をお願い致します。
デザインは下記指示の通りでお願い致します。
枚数は110枚です。
クオリティによっては、報酬額の引き上げも検討できます。
納期は8月23日です。
デザインを確認して、発注という流れでお願い致します。
■依頼詳細
①結婚式招待状
サイズ:縦15〜17cmくらい、横21〜22cmくらい
デザイン:添付写真の様に紺の台紙に金文字にて詳細の記載
デザイン詳細:下の部分に二人のシルエットを描いて頂きたいです。
ひざまづいて花を渡すシーン、背景にはクリスマスツリーを描いてください。

②返信ハガキ
サイズ:普通のハガキサイズ
デザイン:白の用紙に金文字(横書き)
通常の返信ハガキの様に
「出席 欠席 住所 名前」が記載できる様なデザインをお願い致します。
また、下部分には
「会場にて皆様からのメッセージの展示を行います。
新郎新婦に向けて何か一言お書きください」と表記し、メッセージが書ける様にして下さい。韻尾てーしょん

■重視する点
とにかく高級感が出るような色使いをお願い致します。

その他何かご不明な点がございましたら、お気軽にご質問下さい。
よろしくお願いいたします。
サイズ変更です。
以下のサイズで作成をお願い致します。

招待状▶︎角6カマスサイズ(162×229MM)

一番イメージに近く、またフォローも手厚かった為

皆さまご提案ほんとうにありがとうございました!!!

```html
<!DOCTYPE html>
<html lang="ja">
<head>
<meta charset="UTF-8">
<title>返信ハガキ</title>
<link rel="stylesheet" href="https://fonts.googleapis.com/css2?family=Shippori+Mincho:wght@400;500&display=swap">
<style>
  :root {
    --paper: #ffffff;
    --gold: #b39a2c;
    --gold-soft: #d8c77e;
    --gold-faint: #efe6bd;
  }
  html, body {
    margin: 0;
    padding: 0;
    overflow: hidden;
    background: var(--paper);
  }
  .reply-card {
    position: relative;
    width: 816px;
    height: 1200px;
    background: var(--paper);
    font-family: "Shippori Mincho", "Noto Serif JP", serif;
    color: var(--gold);
    overflow: hidden;
  }
  .header-ornament {
    position: absolute;
    left: 204px;
    top: 92px;
    width: 408px;
    height: 42px;
    background: radial-gradient(ellipse at center, var(--gold-soft) 0%, var(--gold-faint) 55%, rgba(255,255,255,0) 75%);
  }
  .attendance {
    position: absolute;
    top: 236px;
    margin: 0;
    font-size: 54px;
    font-weight: 500;
    letter-spacing: 2px;
    line-height: 1;
  }
  .attendance--yes { left: 171px; }
  .attendance--no { left: 403px; }
  .field {
    position: absolute;
    left: 136px;
    width: 571px;
    border-bottom: 2px solid var(--gold-soft);
    font-size: 22px;
    padding-bottom: 8px;
    line-height: 1;
  }
  .field--address { top: 458px; }
  .field--name { top: 582px; }
  .message-prompt {
    position: absolute;
    top: 718px;
    left: 0;
    width: 816px;
    margin: 0;
    text-align: center;
    font-size: 19px;
    letter-spacing: 1px;
  }
  .message-frame {
    position: absolute;
    left: 41px;
    top: 775px;
    width: 734px;
    height: 390px;
  }
  .frame-corner {
    position: absolute;
    width: 56px;
    height: 56px;
    background: radial-gradient(circle at center, var(--gold-soft) 0%, var(--gold-faint) 60%, rgba(255,255,255,0) 80%);
  }
  .frame-corner--tl { left: 0; top: 0; }
  .frame-corner--tr { right: 0; top: 0; }
  .frame-corner--bl { left: 0; bottom: 0; }
  .frame-corner--br { right: 0; bottom: 0; }
  .frame-crest {
    position: absolute;
    left: 307px;
    top: 0;
    width: 120px;
    height: 34px;
    background: radial-gradient(ellipse at center, var(--gold-soft) 0%, var(--gold-faint) 55%, rgba(255,255,255,0) 78%);
  }
</style>
</head>
<body>
  <main class="reply-card">
    <div class="header-ornament" role="img" aria-label="金色の装飾飾り罫"></div>

    <p class="attendance attendance--yes">御出席</p>
    <p class="attendance attendance--no">御欠席</p>

    <div class="field field--address">住所</div>
    <div class="field field--name">名前</div>

    <p class="message-prompt">新郎新婦に向けて何か一言お書きください</p>

    <div class="message-frame">
      <svg width="734" height="390" viewBox="0 0 734 390">
        <rect x="12" y="12" width="710" height="366" fill="none" stroke="var(--gold)" stroke-width="2.5"/>
        <rect x="22" y="22" width="690" height="346" fill="none" stroke="var(--gold)" stroke-width="1"/>
      </svg>
      <div class="frame-crest" role="img" aria-label="枠上部の金色の飾り"></div>
      <div class="frame-corner frame-corner--tl" role="img" aria-label="枠の角の金色の飾り"></div>
      <div class="frame-corner frame-corner--tr" role="img" aria-label="枠の角の金色の飾り"></div>
      <div class="frame-corner frame-corner--bl" role="img" aria-label="枠の角の金色の飾り"></div>
      <div class="frame-corner frame-corner--br" role="img" aria-label="枠の角の金色の飾り"></div>
    </div>
  </main>
</body>
</html>
```